snugSEAL - packaging design for plastic zip-lock mechansim

Looking for packaging designs for my patented product, which provides the ability to lock and close existing plastic bags, which have been opened up (like sugar or flour bag, snack bag, etc.). With applying snugSEAL to any bag once opened, the products can be held safe, locked and dry.
Please check my supporting documentation attached, including logos and packaging description.
The packaging design has to make clear to the customer:
- WHAT is this product for
- how to USA
- what are the BENEFITS and the VALUE
I am looking for a long term cooperation with the winning designer, as I will need multiple variations of the packaging depending on individual product usage. I am thinking of approximately 10 different variations in the future.
Updates
Project Deadline Extended Reason: Extending deadline to receive more designs. Please submit your designs according to my description. Let me know if any questions!This will be a long term cooperation as I will need subsequent designs for alternative product variations in the future. Added Saturday, October 22, 2016
Target Market(s)
All consumers who buy products in the supermarket. In particular when they buy products in bags (like salt, sugar, flour, detergents, snacks, ...)
Industry/Entity Type
Retail
Look and feel
Each slider illustrates characteristics of the customer's brand and the style your logo design should communicate.

```html
<!DOCTYPE html>
<html lang="en">
<head>
<meta charset="utf-8">
<title>snugSEAL – Plastic Extension packaging</title>
<link href="https://fonts.googleapis.com/css2?family=Baloo+2:wght@700;800&family=Roboto+Condensed:wght@400;700&family=Roboto:wght@300;700&display=swap" rel="stylesheet">
<style>
  :root {
    --sky-deep: #4f9be6;
    --sky-mid: #8cc4f2;
    --sky-pale: #d9ecfb;
    --white: #ffffff;
    --navy: #0f2f5c;
    --royal: #1a63c6;
    --royal-dark: #0c3f8f;
    --royal-light: #5aa6ec;
    --panel-blue: #2f66ad;
    --corner-blue: #6fa9e0;
    --yellow: #f4ee1c;
    --strip-grey: #e7ecf1;
    --strip-red: #e8252a;
  }
  * { margin: 0; padding: 0; box-sizing: border-box; }
  html, body { width: 1200px; height: 1000px; overflow: hidden; background: var(--white); }
  .canvas {
    position: relative; width: 1200px; height: 1000px; overflow: hidden;
    background: linear-gradient(180deg, var(--sky-deep) 0%, var(--sky-mid) 30%, var(--sky-pale) 48%, var(--white) 58%, var(--white) 100%);
  }
  .product-art {
    position: absolute;
    background: linear-gradient(180deg, var(--strip-grey) 0%, var(--white) 60%, #f3f6f9 100%);
  }
  .product-art--large { left: 430px; top: 0; width: 770px; height: 470px; clip-path: polygon(0 17%, 100% 0, 100% 70%, 4% 100%); }
  .product-art--small { left: 58px; top: 280px; width: 252px; height: 116px; transform: rotate(-5deg); }
  .product-art--sheet { left: 145px; top: 420px; width: 215px; height: 140px; background: linear-gradient(180deg, #f6f8fa, rgba(255,255,255,0.4)); }

  .label {
    position: absolute; left: 42px; top: 595px; width: 1123px; height: 288px;
    background: radial-gradient(circle at 78% 18%, var(--royal-light) 0%, var(--royal) 45%, var(--royal-dark) 100%);
    box-shadow: 0 0 22px rgba(0,0,0,0.35);
    overflow: hidden;
    font-family: "Roboto Condensed", Arial, sans-serif;
  }
  .label__brand-strip {
    position: absolute; left: 0; top: 0; width: 103px; height: 100%;
    background: var(--navy); border-right: 5px solid #b9cde4;
  }
  .label__brand-name {
    position: absolute; left: 51px; top: 144px; transform: translate(-50%, -50%) rotate(-90deg);
    font-family: "Roboto", sans-serif; font-weight: 300; font-size: 44px; letter-spacing: 2px;
    color: var(--white); white-space: nowrap;
  }
  .label__title {
    position: absolute; left: 150px; top: 14px;
    font-family: "Baloo 2", sans-serif; font-weight: 800; color: var(--white);
    font-size: 76px; line-height: 64px; transform: skewX(-6deg);
    text-shadow: 0 4px 0 var(--navy), 0 6px 8px rgba(0,0,0,0.4);
  }
  .label__title span { display: block; }
  .label__title .line-2 { margin-left: -10px; }
  .label__tagline {
    position: absolute; left: 135px; top: 167px;
    font-family: "Baloo 2", sans-serif; font-weight: 800; font-size: 30px; color: var(--yellow);
    transform: rotate(-4deg) skewX(-12deg); letter-spacing: 1px;
    text-shadow: 0 2px 3px rgba(0,0,0,0.4);
  }
  .label__size {
    position: absolute; left: 203px; top: 252px; font-size: 17px; color: var(--white);
  }
  .label__art {
    position: absolute;
    background: linear-gradient(180deg, var(--strip-grey), var(--white));
  }
  .label__art--large { left: 693px; top: 0; width: 430px; height: 185px; clip-path: polygon(0 25%, 100% 0, 100% 80%, 4% 100%); }
  .label__art--small { left: 553px; top: 121px; width: 95px; height: 32px; transform: rotate(-4deg); }
  .label__art--sheet { left: 586px; top: 165px; width: 84px; height: 90px; }
  .label__stand-box {
    position: absolute; left: 565px; top: 222px; width: 322px; height: 66px;
    background: var(--panel-blue); border-radius: 8px 8px 0 0; transform: skewX(-8deg);
  }
  .label__stand {
    position: absolute; left: 660px; top: 218px; width: 220px; text-align: center; color: var(--white);
    font-family: "Roboto", sans-serif;
  }
  .label__stand-title { font-weight: 700; font-size: 19px; letter-spacing: 0.5px; }
  .label__stand-text { font-family: "Roboto Condensed", sans-serif; font-size: 15px; line-height: 16px; }
  .label__corner { position: absolute; right: 0; bottom: 0; width: 250px; height: 220px; }
  .label__count {
    position: absolute; right: 38px; top: 178px; text-align: center;
    font-family: "Roboto", sans-serif; font-weight: 700; line-height: 1;
  }
  .label__count-number { display: block; font-size: 58px; color: var(--yellow); text-shadow: 0 2px 3px rgba(0,0,0,0.4); }
  .label__count-unit { display: block; font-size: 30px; color: var(--white); font-weight: 400; letter-spacing: 1px; }
</style>
</head>
<body>
<div class="canvas">
  <div class="product-art product-art--large" role="img" aria-label="Close-up rendering of a clear zip-lock strip with red seal line"></div>
  <div class="product-art product-art--small" role="img" aria-label="Small rendering of the zip-lock strip"></div>
  <div class="product-art product-art--sheet" role="img" aria-label="Clear adhesive sheet"></div>

  <section class="label">
    <div class="label__brand-strip">
      <div class="label__brand-name">snugSEAL</div>
    </div>

    <h1 class="label__title"><span>Plastic</span><span class="line-2">Extension</span></h1>
    <p class="label__tagline">ZIP LOCK MECHANISM</p>
    <p class="label__size">10 STRAP 10 in x 0 in (25cm x 00cm</p>

    <div class="label__art label__art--large" role="img" aria-label="Zip-lock strip rendering"></div>
    <div class="label__art label__art--small" role="img" aria-label="Small zip-lock strip rendering"></div>

    <div class="label__stand-box"></div>
    <div class="label__art label__art--sheet" role="img" aria-label="Adhesive sheet"></div>
    <div class="label__stand">
      <div class="label__stand-title">STAND &amp; STICK</div>
      <div class="label__stand-text">stick to your existing<br>plastic or paper bag easily</div>
    </div>

    <svg class="label__corner" viewBox="0 0 250 220" aria-hidden="true">
      <path d="M250 0 L250 220 L0 220 C120 190 220 110 250 0 Z" fill="var(--corner-blue)" opacity="0.6"/>
      <path d="M250 30 L250 220 L30 220 C140 190 230 120 250 30 Z" fill="var(--panel-blue)"/>
    </svg>
    <div class="label__count">
      <span class="label__count-number">10</span>
      <span class="label__count-unit">STRAPS</span>
    </div>
  </section>
</div>
</body>
</html>
```